Can Design for Fun, Growing Health Food Brand

We are launching a brand new product, electrolyte seltzer drinks. We want the design to be clean/simple and slightly modern while staying true to our brand identity. Must say "Mineral Hydration" as the product descriptor, sub headline is "Carbonated electrolyte beverage with sea moss and real fruit juice". First flavors will be Watermelon Mint and Mango.

Target Market(s)

Women ages 30-50 who are interested in health wellness/trends

Industry/Entity Type

Health & Wellness

Font styles to use
Sans Serif

Requirements
Must have
• Tall, skinny can, current Bright Kelp Co Logo, use aluminum on can as element in design.
Nice to have
• Be fun, clean and modern. Would like to see the label less busy than our gels.
Should not have
• Avoid putting flavor on bottom 1/5 of can. No gradient color changes. Do not want really detailed or realistic fruit image, prefer drawings or similar.

```html
<!DOCTYPE html>
<html lang="en">
<head>
<meta charset="utf-8">
<title>Mineral Hydration – Watermelon Mint Can Label</title>
<link href="https://fonts.googleapis.com/css2?family=Montserrat:wght@800&family=Outfit:wght@300;400&display=swap" rel="stylesheet">
<style>
  :root {
    --backdrop: #f1f1f2;
    --alu-light: #fbfbfc;
    --alu-mid: #e4e5e7;
    --alu-dark: #cfd1d4;
    --kelp-green: #1f5e4e;
    --melon-pink: #eaa6b0;
    --melon-text: #d98895;
    --band-text: #ffffff;
  }
  * { margin: 0; padding: 0; box-sizing: border-box; }
  html, body {
    width: 1200px; height: 800px; overflow: hidden;
    background: var(--backdrop);
  }
  .canvas {
    position: relative; width: 1200px; height: 800px;
    display: flex; align-items: center; justify-content: center;
  }
  .can-label {
    position: relative; width: 340px; height: 740px;
    border-radius: 18px; overflow: hidden;
    background: linear-gradient(90deg, var(--alu-dark) 0%, var(--alu-light) 22%, var(--alu-mid) 48%, var(--alu-light) 70%, var(--alu-dark) 100%);
    box-shadow: 0 10px 30px rgba(0,0,0,0.08);
  }
  .claims {
    position: absolute; top: 34px; left: 0; right: 0;
    text-align: center; white-space: nowrap;
    font-family: "Outfit", sans-serif; font-weight: 400;
    font-size: 10px; letter-spacing: 2.4px; color: var(--kelp-green);
  }
  .brand {
    position: absolute; top: 100px; left: 0; right: 0;
    display: flex; flex-direction: column; align-items: center; gap: 8px;
  }
  .brand-dot {
    width: 30px; height: 30px; border-radius: 50%;
    border: 2px solid var(--kelp-green);
  }
  .brand-name {
    font-family: "Outfit", sans-serif; font-weight: 400;
    font-size: 17px; color: var(--kelp-green); letter-spacing: 0.3px;
  }
  .product-title {
    position: absolute; top: 200px; left: 0; right: 0;
    text-align: center;
    font-family: "Montserrat", sans-serif; font-weight: 800;
    font-size: 52px; line-height: 0.98; color: var(--kelp-green);
    letter-spacing: -0.5px;
  }
  .flavor {
    position: absolute; top: 322px; left: 0; right: 0;
    text-align: center;
    font-family: "Outfit", sans-serif; font-weight: 300;
    font-size: 14px; letter-spacing: 2px; color: var(--melon-text);
  }
  .flavor-art {
    position: absolute; top: 370px; left: 75px;
    width: 190px; height: 170px; border-radius: 12px;
    background: radial-gradient(circle at 45% 40%, #eaa6b0 0%, #e9c6cb 45%, #d6e3dd 100%);
  }
  .base-band {
    position: absolute; left: 0; right: 0; bottom: 0; height: 200px;
    background: var(--melon-pink);
  }
  .base-band svg { position: absolute; top: -18px; left: 0; }
  .descriptor {
    position: absolute; top: 42px; left: 40px; right: 40px;
    text-align: center;
    font-family: "Outfit", sans-serif; font-weight: 300;
    font-size: 15px; line-height: 1.25; color: var(--band-text);
  }
  .volume {
    position: absolute; bottom: 36px; left: 0; right: 0;
    text-align: center;
    font-family: "Outfit", sans-serif; font-weight: 400;
    font-size: 14px; color: var(--band-text);
  }
</style>
</head>
<body>
  <main class="canvas">
    <section class="can-label">
      <p class="claims">NO ADDED SUGAR &nbsp;•&nbsp; NATURAL SEA MOSS &nbsp;•&nbsp; PLANT BASED</p>

      <div class="brand">
        <span class="brand-dot"></span>
        <span class="brand-name">Bright Kelp Co</span>
      </div>

      <h1 class="product-title">MINERAL<br>HYDRATION</h1>
      <p class="flavor">— WATERMELON MINT —</p>

      <div class="flavor-art" role="img" aria-label="Line drawing of a watermelon slice with mint leaves and bubbles"></div>

      <div class="base-band">
        <svg width="340" height="20" viewBox="0 0 340 20" aria-hidden="true">
          <path d="M0 20 L0 8 L30 12 L55 4 L80 10 L110 2 L140 9 L170 5 L200 12 L230 3 L260 10 L290 6 L315 11 L340 4 L340 20 Z" fill="var(--melon-pink)"/>
        </svg>
        <p class="descriptor">Carbonated electrolyte beverage with sea moss and real fruit juice</p>
        <p class="volume">335 ml</p>
      </div>
    </section>
  </main>
</body>
</html>
```